KVT Business Cards

We require business cards for our business. We would like a matte black back to the card, with our logo centred in the middle. The front side of the card is open to design.

Target Market(s)

Clients looking for legal services (professional)

Industry/Entity Type

Legal

Contact Information for Business Card

Boris Telemark
Partner
Mobile: 0438 715 642
Email: boris@kvtlaw.co
Website: www.kvtlaw.co
Level 3, 118 Wexbury Street
Sydney NSW 2000

Font styles to use
Other font styles liked:
• Avenir

Colors
f04a50
ffffff
1b1b1b

Requirements
Must have
• Black back with logo included in the centre of the card.
• Our font is Avenir.

```html
<!DOCTYPE html>
<html lang="en">
<head>
<meta charset="utf-8">
<title>KVT Legal Business Card</title>
<link rel="stylesheet" href="https://fonts.googleapis.com/css2?family=Montserrat:wght@500;600;700&display=swap">
<style>
  :root {
    --backdrop: #cbcbcb;
    --brand-red: #ef4a50;
    --paper: #ffffff;
    --ink: #1b1b1b;
    --card-w: 760px;
    --card-h: 465px;
  }
  * { box-sizing: border-box; margin: 0; padding: 0; }
  html, body {
    width: 1200px;
    height: 1200px;
    overflow: hidden;
    background: var(--backdrop);
    font-family: "Montserrat", "Avenir", sans-serif;
  }
  .sheet {
    width: 1200px;
    height: 1200px;
    display: flex;
    flex-direction: column;
    align-items: center;
    justify-content: center;
    gap: 60px;
  }
  .card {
    position: relative;
    width: var(--card-w);
    height: var(--card-h);
    box-shadow: 0 2px 6px rgba(0, 0, 0, 0.18);
  }

  /* Front */
  .card--front { background: var(--brand-red); }
  .holder {
    position: absolute;
    right: 420px;
    top: 160px;
    text-align: right;
  }
  .holder__name {
    font-size: 27px;
    font-weight: 700;
    letter-spacing: 1.5px;
    color: var(--ink);
    white-space: nowrap;
  }
  .holder__role {
    margin-top: 2px;
    font-size: 13px;
    font-weight: 600;
    letter-spacing: 2px;
    color: var(--paper);
  }
  .divider {
    position: absolute;
    left: 360px;
    top: 222px;
  }
  .contact-keys {
    position: absolute;
    left: 398px;
    top: 226px;
    display: flex;
    flex-direction: column;
    font-size: 15px;
    font-weight: 600;
    line-height: 22px;
    color: var(--ink);
  }
  .contact-list {
    position: absolute;
    left: 430px;
    top: 240px;
    list-style: none;
    font-size: 17px;
    font-weight: 600;
    letter-spacing: 2.2px;
    line-height: 26px;
    color: var(--paper);
  }
  .address {
    position: absolute;
    left: 110px;
    bottom: 62px;
    font-size: 14px;
    font-weight: 600;
    letter-spacing: 2px;
    color: var(--paper);
  }

  /* Back: matte black with centred name */
  .card--back { background: var(--ink); }
  .wordmark {
    position: absolute;
    inset: 0;
    display: flex;
    align-items: center;
    justify-content: center;
    gap: 22px;
  }
  .wordmark__square {
    width: 60px;
    height: 60px;
    background: var(--brand-red);
  }
  .wordmark__name {
    font-size: 24px;
    font-weight: 600;
    line-height: 28px;
    letter-spacing: 1px;
    color: var(--paper);
  }
</style>
</head>
<body>
  <main class="sheet">
    <section class="card card--back" aria-label="Card back">
      <div class="wordmark">
        <span class="wordmark__square"></span>
        <p class="wordmark__name">KESTREL<br>VANCE TELEMARK<br>LEGAL</p>
      </div>
    </section>

    <section class="card card--front" aria-label="Card front">
      <div class="holder">
        <h1 class="holder__name">BORIS TELEMARK</h1>
        <p class="holder__role">PARTNER</p>
      </div>
      <svg class="divider" width="24" height="84" viewBox="0 0 24 84" aria-hidden="true">
        <line x1="20" y1="2" x2="4" y2="82" stroke="var(--ink)" stroke-width="3.5" stroke-linecap="round"/>
      </svg>
      <div class="contact-keys" aria-hidden="true">
        <span>M</span><span>E</span><span>W</span>
      </div>
      <ul class="contact-list">
        <li>0438 715 642</li>
        <li>boris@kvtlaw.co</li>
        <li>www.kvtlaw.co</li>
      </ul>
      <p class="address">Level 3, 118 Wexbury Street Sydney NSW 2000</p>
    </section>
  </main>
</body>
</html>
```